LA's Newest HEMP Facial Oil and Body Oil Packaging Project

We need a packaging concept for a Hemp based facial oil and body oil. We need label design for the bottle and carton graphics. I am attaching a few reference photos. The target demographic is women between 17-35 year old. Products need to be able to stand out in crowded stores with clear calls to action.
1oz Dropper Bottle with Unit Carton - Hemp Facial Oil
4oz PET Bottle with Unit Carton - Hemp + Rose Facial Oil

```html
<!DOCTYPE html>
<html lang="en">
<head>
<meta charset="utf-8">
<title>Hemp Body Oil and Facial Oil Packaging</title>
<link rel="stylesheet" href="https://fonts.googleapis.com/css2?family=Bebas+Neue&family=Montserrat:wght@400;500;700&display=swap">
<style>
  :root {
    --page: #ffffff;
    --kraft: #d3b18d;
    --ink: #2a2723;
    --leaf-soft: #a88b66;
    --gold-dark: #8c6c2c;
    --gold-mid: #c9ab62;
    --gold-light: #efe2b2;
  }
  * { box-sizing: border-box; margin: 0; padding: 0; }
  html, body { width: 1200px; height: 969px; overflow: hidden; background: var(--page); }
  .canvas { position: relative; width: 1200px; height: 969px; }

  .panel {
    position: absolute;
    background: var(--kraft);
    color: var(--ink);
    text-align: center;
    overflow: hidden;
  }
  .panel > * { position: absolute; left: 0; right: 0; }

  .label-body   { left: 98px;  top: 506px; width: 214px; height: 302px; }
  .carton-front { left: 408px; top: 105px; width: 273px; height: 729px; }
  .label-facial { left: 726px; top: 526px; width: 192px; height: 276px; }

  .leaf-art {
    background: linear-gradient(180deg, var(--leaf-soft), var(--kraft));
    opacity: 0.85;
  }

  .product-word {
    font-family: "Bebas Neue", sans-serif;
    font-weight: 400;
    color: var(--ink);
    line-height: 1;
    letter-spacing: 2px;
  }
  .product-name {
    font-family: "Bebas Neue", sans-serif;
    font-weight: 400;
    letter-spacing: 3px;
    line-height: 1;
  }
  .with-line, .ingredient-line {
    font-family: "Montserrat", sans-serif;
    font-weight: 500;
    letter-spacing: 3px;
    line-height: 1;
  }
  .skin-band {
    font-family: "Montserrat", sans-serif;
    font-weight: 700;
    line-height: 1;
    display: flex; align-items: center; justify-content: center;
  }
  .skin-band.gilded {
    background: linear-gradient(90deg, var(--gold-dark) 0%, var(--gold-mid) 30%, var(--gold-light) 70%, var(--gold-mid) 100%);
  }
  .size-note {
    font-family: "Montserrat", sans-serif;
    font-weight: 400;
    letter-spacing: 1px;
    line-height: 1;
  }

  /* body oil label */
  .label-body .leaf-art { top: 0; height: 84px; }
  .label-body .product-word { top: 44px; font-size: 52px; }
  .label-body .product-name { top: 128px; font-size: 44px; }
  .label-body .with-line { top: 176px; font-size: 10px; }
  .label-body .ingredient-line { top: 199px; font-size: 10px; }
  .label-body .skin-band { top: 241px; height: 25px; font-size: 13px; padding-left: 16px; }
  .label-body .size-note { top: 277px; font-size: 12px; }

  /* carton front */
  .carton-front .product-word { top: 108px; font-size: 64px; }
  .carton-front .product-name { top: 232px; font-size: 56px; letter-spacing: 6px; }
  .carton-front .with-line { top: 304px; font-size: 14px; letter-spacing: 4px; }
  .carton-front .ingredient-line { top: 335px; font-size: 14px; letter-spacing: 4.5px; }
  .carton-front .leaf-art { top: 379px; height: 296px; right: 8px; border-radius: 0 60% 40% 0; }
  .carton-front .skin-band { top: 683px; height: 16px; font-size: 13px; }
  .carton-front .size-note { top: 713px; font-size: 12px; }

  /* facial oil label */
  .label-facial .leaf-art { top: 0; height: 50px; }
  .label-facial .product-word { top: 56px; font-size: 48px; }
  .label-facial .product-name { top: 136px; font-size: 24px; letter-spacing: 1.5px; }
  .label-facial .skin-band { top: 216px; height: 22px; font-size: 12px; }
  .label-facial .size-note { top: 249px; font-size: 11px; }
</style>
</head>
<body>
<main class="canvas">

  <section class="panel label-body" aria-label="Body oil bottle label">
    <div class="leaf-art" role="img" aria-label="Illustrated hemp leaves along the top of the label"></div>
    <p class="product-word">HEMP</p>
    <h2 class="product-name">BODY OIL</h2>
    <p class="with-line">WITH</p>
    <p class="ingredient-line">HEMP&amp;TEATREE</p>
    <p class="skin-band gilded">ALL SKIN TYPES</p>
    <p class="size-note">4 OZ</p>
  </section>

  <section class="panel carton-front" aria-label="Body oil unit carton front">
    <p class="product-word">HEMP</p>
    <h1 class="product-name">BODY OIL</h1>
    <p class="with-line">WITH</p>
    <p class="ingredient-line">HEMP&amp;TEATREE</p>
    <div class="leaf-art" role="img" aria-label="Large illustrated hemp leaf rising from the lower left of the carton"></div>
    <p class="skin-band">ALL SKIN TYPES</p>
    <p class="size-note">4 OZ</p>
  </section>

  <section class="panel label-facial" aria-label="Facial oil bottle label">
    <div class="leaf-art" role="img" aria-label="Row of illustrated hemp leaves along the top of the label"></div>
    <p class="product-word">HEMP</p>
    <h2 class="product-name">FACIAL OIL</h2>
    <p class="skin-band gilded">ALL SKIN TYPES</p>
    <p class="size-note">1 OZ</p>
  </section>

</main>
</body>
</html>
```